Business card for STEADYLINE

Please design professional business card for IT consulting firm STEADYLINE INC.
Use logo attached.
Use information from sample tRove business card attached.
replace trove inc with STEADYLINE INC.
as well as troveinc.com with steadyline.example

```html
<!DOCTYPE html>
<html lang="en">
<head>
<meta charset="utf-8">
<title>STEADYLINE business card</title>
<link rel="stylesheet" href="https://fonts.googleapis.com/css2?family=Roboto+Condensed:wght@300;400;700&display=swap">
<style>
  :root {
    --page: #ffffff;
    --card-dark: #08090b;
    --card-light: #ffffff;
    --ink-light: #ffffff;
    --ink-dark: #0b0b0c;
    --ink-muted: #8e8e8e;
    --accent: #f28a1f;
    --accent-deep: #d9701a;
  }
  * { margin: 0; padding: 0; box-sizing: border-box; }
  html, body {
    width: 1200px; height: 951px; overflow: hidden;
    background: var(--page);
    font-family: "Roboto Condensed", sans-serif;
  }
  .canvas { position: relative; width: 1200px; height: 951px; }

  .card {
    position: absolute; left: 365px; width: 483px; height: 283px;
    overflow: hidden;
  }
  .card--front { top: 155px; background: var(--card-dark); color: var(--ink-light); }
  .card--back {
    top: 543px; background: var(--card-light); color: var(--ink-dark);
    box-shadow: 0 6px 24px rgba(0,0,0,0.07);
  }

  .accent-band {
    position: absolute; left: 0; top: 0; width: 29px; height: 100%;
    background: linear-gradient(to bottom, var(--accent), var(--accent-deep));
  }

  .brand {
    position: absolute; display: flex; align-items: center;
    font-weight: 700; letter-spacing: 0.14em; white-space: nowrap;
  }
  .brand__square { background: var(--accent); margin-left: 0.3em; }
  .card--front .brand { right: 32px; top: 30px; font-size: 26px; line-height: 30px; }
  .card--front .brand__square { width: 10px; height: 10px; }
  .card--back .brand { left: 49px; top: 48px; font-size: 31px; line-height: 34px; }
  .card--back .brand__square { width: 12px; height: 12px; }

  .line { position: absolute; white-space: nowrap; }
  .card--front .line { left: 42px; }
  .card--back .line { left: 50px; }

  .job-title { font-weight: 300; font-size: 13.5px; line-height: 16px; letter-spacing: 0.01em; }
  .card--back .job-title { color: var(--ink-muted); }
  .person-name { font-weight: 700; font-size: 18.5px; line-height: 22px; letter-spacing: -0.01em; }
  .person-name__cred { font-size: 12.5px; }
  .detail { font-weight: 300; font-size: 12.3px; line-height: 15px; }
  .company { font-weight: 700; font-size: 11.5px; line-height: 15px; }

  .detail__col2 { position: absolute; left: 135px; }
  .detail__col3 { position: absolute; left: 172px; }
</style>
</head>
<body>
<main class="canvas">

  <section class="card card--front" aria-label="Business card front">
    <div class="accent-band"></div>
    <div class="brand">STEADYLINE<span class="brand__square"></span></div>

    <p class="line job-title" style="top:132px">GENERAL MANAGER</p>
    <p class="line person-name" style="top:148px">MAREK SOLANOV, <span class="person-name__cred">P. ENG.</span></p>
    <p class="line detail" style="top:171px">o: (555) 014-2030 ext.201<span class="detail__col2">c: (555) 019-4477</span></p>
    <p class="line detail" style="top:186px">e: msolanov@steadyline.example<span class="detail__col3">www.steadyline.example</span></p>
    <p class="line company" style="top:213px">STEADYLINE.EXAMPLE</p>
    <p class="line detail" style="top:227px">1280 Harbour Ln. Suite 101</p>
    <p class="line detail" style="top:242px">Milton Heights, Ontario, K0A 1B2, Canada</p>
  </section>

  <section class="card card--back" aria-label="Business card back">
    <div class="brand">STEADYLINE<span class="brand__square"></span></div>

    <p class="line job-title" style="top:97px">GENERAL MANAGER</p>
    <p class="line person-name" style="top:116px">MAREK SOLANOV, <span class="person-name__cred">P. ENG.</span></p>
    <p class="line detail" style="top:143px">o: (555) 014-2030 ext.201<span class="detail__col2">c: (555) 019-4477</span></p>
    <p class="line detail" style="top:158px">e: msolanov@steadyline.example<span class="detail__col3">www.steadyline.example</span></p>
    <p class="line company" style="top:185px">STEADYLINE.EXAMPLE</p>
    <p class="line detail" style="top:200px">1280 Harbour Ln. Suite 101</p>
    <p class="line detail" style="top:214px">Milton Heights, Ontario, K0A 1B2, Canada</p>
  </section>

</main>
</body>
</html>
```